The Bramblewood Roadside Defense Guide
An Owner's Notes on Quietly Settling Every Old Dispute
The Bramblewood Roadside Defense Guide - Law
This book will be read by middle class, well educated people with pending reckless driving charges.
Dimensions are approximately 6.5" x 8.5" (half sheet). We would like the title, sub title and the author's name ( Owen T. Marsh) to appear on the front cover. No text on the spine (about 1/8" spine). The back page will have no text. but the design on the back cover should allow us to place a text layer on top of the back cover design - so the back cover design should not make it difficult to read the text. (See attached example from previous project)
omarsh omarsh
#99 #100 #101 Submissions should not have any text on the back cover. Please remove the text from the back cover if you want your submission to be considered.
#61 - Can you do some variations of the text. Perhaps tweak the color or the color gradient.
#36 #66 #61 #45 #42 #53 #45 These are the top contenders. These are all awesome designs! To be selected the design must include back and front covers and NOT contain "2nd edition"
#36 #66 #61 #45 To be considered you must have a back cover as well as a front cover. Please resubmit your design with a back cover
#61 Can you take off the "2nd edition" from the front - this is not the second edition.
#14 my wife likes this one so that is a plus.:)
#7 this looks like a book on Velvet Harbor - Awesome! but probably not a great angle for a law firm :) I wonder if they would sue me if we just put a crystal pyramid and rainbow on the cover?
#11 nice design but too similar to the DUI book cover.
#14 Reckless driving cases are 80% speed related so the cover matches the subject well and it breaks away from the frame clip art pack nicely. The is something about it that says "Car ad" rather than legal book though. Maybe its the bright colors and contemporary "smart car" looking vehicle. May be look for different versions of the same theme and see.
#23 - forgot the title.
#20 I like the dirty scratched texture you did in #8 better, it makes it seem more interesting. #8's texturing is pretty heavy though, a slightly toned version, something in between #8 and #20 might be a good idea, no 100% sure though. I still think there needs to be some original graphic on the cover instead of just the text or framed clip art.
#9 I like that you are creating original images instead of just using the clip art whole-cloth and getting rid of the borders. That doesn't mean that a submission couldn't have a square frame clip art, it just means that originality scores points.
#22 Not bad, but the simplicity takes away from the professionalism. The look is not bad but then you realize its just swirled sirens with the clip art pasted on top. If the cover image was something original or it used some original elements in it I think it would help overcome that. I really like that your submissions are all over the place and not just a different versions of the same thing.
#19 I like that concept of this design. Its abstract, not just clip art photography pastes on the cover. Its completely unique from the other too examples of book covers. The colors and text are not my favorite. So the execution is not there yet but the fact that it is completely going off on its own is a big plus.
#8 I like the design of the scratched surface and the yellow hash marks...but it seems a little off. I don't know that the clip art I uploaded really matches. I can't help but wonder if something with traffic cones or a speed limit sign might be better. Don't know for sure...just vague impressions.
#21 this looks too similar to what we already have and is not very contemporary. Keep trying though.
#18 is a bit too similar to the DUI book cover I uploaded as an example. I don't want to be derivative.
#1 I think the police tap doesn't really match the Reckless driving. Most reckless driving cases are for speeding or minor car accidents, falling asleep at the wheel or someone doing doughnuts in a parking lot. Police crime scene tape doesn't usually come into play.
#2,#,3,#4 I marked these low because this is a reckless driving book not DUI. Reckless driving is not generally an alcohol offense in Va and so the covers' designs were a bit confusing.

```html
<!DOCTYPE html>
<html lang="en">
<head>
<meta charset="utf-8">
<title>The Bramblewood Roadside Defense Guide – Cover Spread</title>
<link href="https://fonts.googleapis.com/css2?family=Arimo:wght@400;700&display=swap" rel="stylesheet">
<style>
  :root {
    --page-bg: #e8e8e8;
    --guide: #c4c4c4;
    --label: #8a8a8a;
    --sky-deep: #1f4f9a;
    --sky-mid: #4d83c6;
    --sky-light: #d6e5f4;
    --field: #3f6a2c;
    --field-dark: #24401b;
    --road: #3d4247;
    --road-dark: #22262a;
    --title-ink: #0b1a2e;
    --white: #ffffff;
  }
  * { margin: 0; padding: 0; box-sizing: border-box; }
  html, body { width: 1200px; height: 936px; overflow: hidden; }
  body { background: var(--page-bg); position: relative; font-family: "Arimo", Arial, sans-serif; }

  .size-label {
    position: absolute; left: 13px; top: 26px;
    font-size: 21px; color: var(--label);
  }
  .spine-label {
    position: absolute; left: 553px; top: 828px;
    font-size: 21px; color: var(--label);
  }
  .guide { position: absolute; background: var(--guide); }
  .guide--v { width: 1px; top: 90px; height: 760px; }
  .guide--h { height: 1px; left: 90px; width: 1036px; }

  .spread {
    position: absolute; left: 114px; top: 114px; width: 987px; height: 706px; overflow: hidden;
  }
  .scene {
    position: absolute; inset: 0;
    background:
      radial-gradient(ellipse 45% 30% at 62% 62%, rgba(255,255,255,0.85), rgba(255,255,255,0) 70%),
      radial-gradient(ellipse 70% 50% at 55% 40%, rgba(214,229,244,0.9), rgba(214,229,244,0) 75%),
      linear-gradient(to bottom,
        var(--sky-deep) 0%, var(--sky-mid) 30%, var(--sky-light) 55%,
        #b9cbb8 61%, var(--field) 64%, var(--field-dark) 72%,
        var(--road) 78%, var(--road-dark) 100%);
  }

  .back-cover {
    position: absolute; left: 51px; top: 0; width: 405px; height: 706px;
  }
  .author-photo {
    position: absolute; left: 299px; top: 69px; width: 76px; height: 106px; background: var(--white);
  }
  .back-rule {
    position: absolute; top: 317px; left: 0; width: 405px; height: 1px; background: rgba(255,255,255,0.8);
  }
  .code-area {
    position: absolute; left: 8px; top: 541px; width: 93px; height: 93px; background: var(--white);
  }

  .front-cover {
    position: absolute; left: 494px; top: 0; width: 493px; height: 706px;
  }
  .title {
    position: absolute; top: 90px; left: 0; width: 475px; text-align: center;
    font-weight: 700; color: var(--title-ink); line-height: 1;
  }
  .title-lead { display: block; font-size: 34px; }
  .title-main {
    display: block; font-size: 84px; line-height: 0.92; letter-spacing: -1px;
    text-shadow: 0 0 3px rgba(255,255,255,0.9), 0 0 1px #fff;
  }
  .title-lead + .title-main { margin-top: 4px; }
  .title-tail { display: block; font-size: 32px; margin-top: 2px; }
  .subtitle {
    position: absolute; top: 350px; left: 0; width: 475px; text-align: center;
    font-size: 19px; line-height: 27px; color: var(--white);
  }
  .author-name {
    position: absolute; top: 628px; right: 160px;
    font-size: 19px; color: var(--white);
  }
</style>
</head>
<body>
  <div class="size-label">Book Cover 6.5" x 8.5</div>

  <div class="guide guide--v" style="left:114px"></div>
  <div class="guide guide--v" style="left:600px"></div>
  <div class="guide guide--v" style="left:611px"></div>
  <div class="guide guide--v" style="left:1101px"></div>
  <div class="guide guide--h" style="top:114px"></div>
  <div class="guide guide--h" style="top:820px"></div>

  <main class="spread">
    <div class="scene" role="img" aria-label="Photograph of an open country road under a bright blue cloudy sky, green fields at the horizon, with a roadside welcome sign"></div>

    <section class="back-cover" aria-label="Back cover, left clear for a text layer">
      <div class="author-photo"></div>
      <div class="back-rule"></div>
      <div class="code-area"></div>
    </section>

    <section class="front-cover">
      <h1 class="title">
        <span class="title-lead">The Bramblewood</span>
        <span class="title-main">Roadside</span>
        <span class="title-main">Defense</span>
        <span class="title-tail">Guide</span>
      </h1>
      <p class="subtitle">An Owner's Notes<br>on Quietly Settling<br>Every Old Dispute</p>
      <p class="author-name">Owen T. Marsh, Esq.</p>
    </section>
  </main>

  <div class="spine-label">1/8" spine</div>
</body>
</html>
```